Redesign business cards

We have a new logo and I am not that happy with the layout of our existing card and looking for a change. Font is a bit small and the green can be hard to read. Logo may need a tidy up as the copy I have is not that hi-res too so require you to produce a hi-res version of the logo for us too. There will be three individual business cards to produce with just the names and phone numbers being different. Address will change too, but use what you see on the card for now.

Industry/Entity Type

Business

Requirements
Nice to have
• You could consider a redesign to the new logo, just not too radical. We like the blue and green hexagons as we feel that they are representative of oil industry that we are in.

```html
<!DOCTYPE html>
<html lang="en">
<head>
<meta charset="utf-8">
<title>NovaLube Oil Services – Business Card</title>
<link rel="stylesheet" href="https://fonts.googleapis.com/css2?family=Asap:wght@400;700&family=Marcellus&display=swap">
<style>
  :root {
    --page-bg: #eeeeee;
    --card-bg: #ffffff;
    --brand-green: #9bcc0a;
    --brand-blue: #12b4e2;
    --ink: #111111;
    --band-text: #ffffff;
  }
  * { box-sizing: border-box; margin: 0; padding: 0; }
  html, body {
    width: 1200px;
    height: 777px;
    overflow: hidden;
    background: var(--page-bg);
  }
  .canvas {
    position: relative;
    width: 1200px;
    height: 777px;
  }
  .card {
    position: absolute;
    left: 50px;
    top: 89px;
    width: 1100px;
    height: 598px;
    background: var(--card-bg);
    box-shadow: 0 2px 6px rgba(0,0,0,0.15);
    overflow: hidden;
  }
  .brand {
    position: absolute;
    left: 54px;
    top: 118px;
    display: flex;
    align-items: flex-start;
    gap: 14px;
    color: var(--brand-green);
    font-family: "Asap", sans-serif;
    font-weight: 700;
  }
  .brand-dot {
    width: 22px;
    height: 22px;
    margin-top: 14px;
    border-radius: 50%;
    background: var(--brand-blue);
  }
  .brand-name {
    font-size: 76px;
    line-height: 0.95;
    letter-spacing: -1px;
  }
  .brand-tagline {
    display: block;
    font-size: 30px;
    line-height: 1.2;
    letter-spacing: 0;
  }
  .person {
    position: absolute;
    left: 54px;
    top: 278px;
    font-family: "Asap", sans-serif;
    font-weight: 400;
    font-size: 30px;
    line-height: 46px;
  }
  .person-name { color: var(--brand-blue); }
  .person-role { color: var(--brand-green); }
  .divider {
    position: absolute;
    left: 622px;
    top: 120px;
    width: 2px;
    height: 325px;
    background: var(--brand-green);
  }
  .contact {
    position: absolute;
    left: 658px;
    top: 206px;
    list-style: none;
    font-family: "Marcellus", serif;
    font-size: 29px;
    color: var(--ink);
  }
  .contact li { height: 57px; line-height: 40px; }
  .address-band {
    position: absolute;
    left: 0;
    bottom: 0;
    width: 100%;
    height: 86px;
    background: linear-gradient(to right, var(--brand-green) 0 548px, var(--brand-blue) 548px 100%);
    display: flex;
    align-items: center;
    padding-left: 24px;
    font-family: "Marcellus", serif;
    font-size: 21px;
    color: var(--band-text);
    white-space: nowrap;
  }
  .address-band .sep { margin: 0 4px; }
</style>
</head>
<body>
<main class="canvas">
  <section class="card">
    <div class="brand">
      <span class="brand-name">NovaLube<span class="brand-tagline">Oil Services</span></span>
      <span class="brand-dot" aria-hidden="true"></span>
    </div>

    <div class="person">
      <p class="person-name">Daniel Hartwell NZCE (Mech) P&amp;P</p>
      <p class="person-role">Director</p>
    </div>

    <div class="divider" aria-hidden="true"></div>

    <ul class="contact">
      <li>P : +614 555 01847</li>
      <li>E : daniel@novalube.co.nz</li>
      <li>W : www.novalube.com.au</li>
    </ul>

    <footer class="address-band">
      Novalube Oil Services 512 Harbour Road<span class="sep">|</span>PO Box 4471<span class="sep">|</span>Kelvin Grove Queensland 4059
    </footer>
  </section>
</main>
</body>
</html>
```